Thank you for exploring whether you are interested in creating a book cover for The Insight Lantern!

The cover should look professional yet appeal to a person who is open to approaching life more deeply.

The logo that I've uploaded is something that you are welcome to use in your book cover design but is not required to be the primary graphic.

The following is a description of The Insight Lantern and its purpose.
RADICAL CLARITY IS POSSIBLE

Are you tired of hitting up against your limitations? Do you wish you could be more effective in everything you do? What would it be like if you could walk confidently into any situation and automatically comprehend it, organize your thoughts, and respond creatively? This kind of radical clarity is not only possible, it’s right in front of you—and The Insight Lantern: Notice Every Signal. Hold Bold Dialogues. Build the Path You Choose. shows you the pathway to get there!

In the book, Dr. Gavin Terlecki draws on over 30 years of experience with executive coaching and leadership development to deliver priceless wisdom about how to see clearly in today’s complex and uncertain world. Using his Insight Lantern, you’ll discover where you’re stuck and why, find your authentic direction, and learn to engage creatively with life so you can start getting what you really want.

A TRANSFORMATIONAL TOOL

The Insight Lantern is a cutting-edge leadership development tool that supports you to activate your maximum potential, both personally and professionally. It’s based on the idea that there are four fundamental building blocks to reality: Intentions, Actions, Facts, and Stories. Understanding the differences between these dimensions of your experience and learning how they work together is the key to forging a clear path toward your destination in life. The Insight Lantern organizes these four main building blocks around the two polarities of a compass:

1. North to South – Intentions to Actions
We all have billions of intentions, but how many do we actually put into action? In this polarity you learn to notice and implement your intentions in order to generate more effective actions and create meaningful outcomes in your life.

2. East vs. West – Facts vs. Stories
We all create stories to make sense of life, but how many of us actually get clear on the facts to see where our stories might be off? In this polarity you learn to discern the objective facts from your subjective interpretations and stories, illuminating a clearer perspective to uncover what’s been blocking you on the path to success.

Using The Insight Lantern you’ll discover how naming and implementing your intentions in life naturally results in more effective behavior and actions, and how distinguishing the real facts from your interpretations of any situation can propel you toward radical clarity and true fulfillment.

BOLD DIALOGUES

The key benefit of using The Insight Lantern is that you’ll have more of what Gavin calls “Bold Dialogues.” Bold Dialogues are those that move you closer to what you’re wanting in life—the kind of human-to-human interactions that actually make a difference. By applying The Insight Lantern, you gain critical insight that opens your eyes to new opportunities for Bold Dialogues, helping you draw on your imagination and move beyond your current stance toward a positive outcome. Every conversation is a possibility waiting to be discovered. The more Bold Dialogues you have, the more profound and meaningful shifts you activate in your life.

PRACTICAL GUIDANCE

The book doesn’t just give you a theoretical understanding of how to gain more clarity in your life. Dr. Terlecki provides you with clear, practical steps to develop the core competencies you need to start getting the results you want. As you explore the book, you’ll find:

• A thorough description of all the directions of The Insight Lantern, each with three main points to focus your energy on.
• Case studies from Gavin’s many clients who have successfully used The Insight Lantern to transform their own lives.
• Hands-on practices Gavin has developed to help you put your new skills to use immediately.
• Step-by-step guidance to apply The Insight Lantern in any situation, including real-life stories from people who have experienced genuine transformation using this tool.

The Insight Lantern will help you to deepen your understanding of the challenges in your life, integrate new competencies to boost your effectiveness, and awaken to exciting opportunities for your own growth, leadership, and success!

ABOUT THE AUTHOR

Dr. Gavin Terlecki has over 30 years of experience with leadership development and executive coaching work. As owner and principal coach of Terlecki Growth Advisors, he has been integrating the fields of management consulting, business psychology, and leadership coaching since 1983. Gavin holds a Ph.D. in psychodynamic and group psychology from the Halvern Graduate Academy, an M.A. in human growth and potential from the Marlowe Ridge University, and a B.A. in accounting and Business Administration from Denby Valley University. He is the creator of The Insight Lantern™, a leadership development tool that supports people to see life clearly, wake up to exciting opportunities for their own growth and leadership, and take empowered action toward true success. Gavin’s combination of business expertise, human compassion, and incisive questions help his clients achieve unprecedented results.

Target Market(s)

Out intended audience is folks who would like to be more effective and to grow and transform. This being more productive and developing could be in their careers or their personal lives.

Industry/Entity Type

It Professional

Requirements
Must have
• Stock images, if used, that I can purchase exclusively or that you can easily create specifically for the book once you are the chosen designer. I completely understand using stock imaging in your submissions pre-selection.
Nice to have
• Ideally the cover will include both the title and subtitle.

```html
<!DOCTYPE html>
<html lang="en">
<head>
<meta charset="utf-8">
<title>The Insight Lantern — Book Cover Spread</title>
<link rel="stylesheet" href="https://fonts.googleapis.com/css2?family=Cinzel:wght@400;700&family=Tinos:ital,wght@0,400;0,700;1,400&display=swap">
<style>
  :root {
    --page-bg: #ffffff;
    --sky-top: #f4e6d6;
    --sky-glow: #f7dcc4;
    --horizon: #e9c6b4;
    --sea: #d9b7a6;
    --sand-light: #f1d1aa;
    --sand-mid: #e8b98a;
    --sand-deep: #d89a68;
    --ink: #1c1815;
    --ink-soft: #2b2521;
    --rule: #1c1815;
    --object-dark: #2a3147;
    --object-mid: #48506a;
  }
  * { margin: 0; padding: 0; box-sizing: border-box; }
  html, body {
    width: 1200px; height: 1200px; overflow: hidden;
    background: var(--page-bg);
  }
  .canvas { position: relative; width: 1200px; height: 1200px; }

  .spread {
    position: absolute; left: 12px; top: 175px; width: 1176px; height: 815px;
    overflow: hidden;
  }
  .beach-scene {
    position: absolute; inset: 0;
    background:
      radial-gradient(ellipse 60% 18% at 62% 33%, rgba(255,240,225,0.9), rgba(255,240,225,0) 70%),
      linear-gradient(180deg,
        var(--sky-top) 0%, var(--sky-glow) 22%, var(--horizon) 32%,
        var(--sea) 38%, var(--sand-light) 50%, var(--sand-mid) 75%, var(--sand-deep) 100%);
  }

  /* Back cover */
  .back-cover {
    position: absolute; left: 34px; top: 70px; width: 512px;
    font-family: "Tinos", "Times New Roman", serif;
    font-size: 11.4px; line-height: 15.5px; color: var(--ink);
    text-align: justify;
  }
  .back-cover p { margin-bottom: 15px; }
  .back-cover .gap { margin-top: 28px; }
  .feature-list { list-style: disc; padding-left: 26px; margin-bottom: 15px; }
  .feature-list li { margin-bottom: 1px; }
  .author-bio { margin-top: 58px; }

  /* Spine */
  .spine {
    position: absolute; left: 557px; top: 0; width: 70px; height: 815px;
  }
  .spine-title, .spine-author {
    position: absolute; writing-mode: vertical-rl;
    font-family: "Cinzel", "Times New Roman", serif; color: var(--ink);
    letter-spacing: 1.5px;
  }
  .spine-title { left: 8px; top: 30px; font-size: 23px; }
  .spine-author { left: 38px; top: 478px; font-size: 23px; }

  /* Front cover */
  .front-cover { position: absolute; left: 627px; top: 0; width: 549px; height: 815px; }
  .tool-mark {
    position: absolute; left: 0; width: 549px; top: 38px; text-align: center;
    font-family: "Cinzel", "Times New Roman", serif; font-size: 12px; color: var(--ink);
    letter-spacing: 1px;
  }
  .tool-mark .dot {
    display: inline-block; width: 9px; height: 9px; border-radius: 50%;
    background: var(--ink); margin-right: 6px; vertical-align: middle;
  }
  .title-kicker {
    position: absolute; top: 136px; left: 0; width: 549px;
    display: flex; align-items: center; justify-content: center; gap: 18px;
    font-family: "Cinzel", "Times New Roman", serif; font-size: 30px; letter-spacing: 6px;
    color: var(--ink);
  }
  .title-kicker .rule { width: 92px; height: 2px; background: var(--rule); }
  .title-main {
    position: absolute; top: 180px; left: 0; width: 549px; text-align: center;
    font-family: "Cinzel", "Times New Roman", serif; font-weight: 400;
    font-size: 74px; line-height: 84px; color: var(--ink); letter-spacing: 1px;
  }
  .subtitle {
    position: absolute; top: 333px; left: 0; width: 549px; text-align: center;
    font-family: "Cinzel", "Times New Roman", serif; font-size: 17px; line-height: 23px;
    letter-spacing: 2px; color: var(--ink-soft);
  }
  .compass-object {
    position: absolute; left: 262px; top: 475px; width: 222px; height: 212px;
  }
  .author-name {
    position: absolute; top: 756px; left: 0; width: 549px; text-align: center;
    font-family: "Cinzel", "Times New Roman", serif; font-weight: 700;
    font-size: 25px; letter-spacing: 2px; color: var(--ink-soft);
  }
</style>
</head>
<body>
<div class="canvas">
  <div class="spread">
    <div class="beach-scene" role="img" aria-label="Soft-focus photograph of a sandy beach at sunrise with a pastel sky over the sea"></div>

    <section class="back-cover">
      <p>Are you tired of hitting up against your limitations? Do you wish you could be more effective in everything you do? What would it be like if you could walk confidently into any situation and automatically comprehend it, organize your thoughts, and respond creatively? This kind of radical clarity is not only possible, it’s right in front of you—and The Insight Lantern: Notice Every Signal. Hold Bold Dialogues. Build the Path You Choose. shows you the pathway to get there!</p>
      <p>In the book, Dr. Gavin Terlecki draws on over 30 years of experience with executive coaching and leadership development to deliver priceless wisdom about how to see clearly in today’s complex and uncertain world. Using his Insight Lantern, you’ll discover where you’re stuck and why, find your authentic direction, and learn to engage creatively with life so you can start getting what you really want.</p>
      <p class="gap">The book doesn’t just give you a theoretical understanding of how to gain more clarity in your life. Dr. Terlecki provides you with clear, practical steps to develop the core competencies you need to start getting the results you want. As you explore the book, you’ll find:</p>
      <ul class="feature-list">
        <li>A thorough description of all the directions of the Insight Lantern, each with three main points to focus your energy on.</li>
        <li>Case studies from Gavin’s many clients who have successfully used the Insight Lantern to transform their own lives.</li>
        <li>Hands-on practices Gavin has developed to help you put your new skills to use immediately.</li>
        <li>Step-by-step guidance to apply the Insight Lantern in any situation, including real-life stories from people who have experienced genuine transformation using this tool.</li>
      </ul>
      <p>The Insight Lantern will help you to deepen your understanding of the challenges in your life, integrate new competencies to boost your effectiveness, and awaken to exciting opportunities for your own growth, leadership, and success!</p>
      <p class="author-bio"><strong>Dr. Gavin Terlecki</strong> has over 30 years of experience with leadership development and executive coaching work. As owner and principal coach of Terlecki Growth Advisors, he has been integrating the fields of management consulting, business psychology, and leadership coaching since 1983. Gavin holds a Ph.D. in psychodynamic and group psychology from the Halvern Graduate Academy, an M.A. in human growth and potential from the Marlowe Ridge University, and a B.A. in accounting and Business Administration from Denby Valley University. He is the creator of the Insight Lantern™, a leadership development tool that supports people to see life clearly, wake up to exciting opportunities for their own growth and leadership, and take empowered action toward true success. Gavin’s combination of business expertise, human compassion, and incisive questions help his clients achieve unprecedented results.</p>
    </section>

    <div class="spine">
      <div class="spine-title">THE INSIGHT LANTERN</div>
      <div class="spine-author">DR. GAVIN TERLECKI</div>
    </div>

    <section class="front-cover">
      <div class="tool-mark"><span class="dot"></span>Insight Lantern</div>
      <div class="title-kicker"><span class="rule"></span>THE<span class="rule"></span></div>
      <h1 class="title-main">INSIGHT<br>LANTERN</h1>
      <p class="subtitle">Notice Every Signal.<br>Hold Bold Dialogues.<br>Build the Path You Choose.</p>
      <svg class="compass-object" viewBox="0 0 222 212" role="img" aria-label="Photograph of a pocket compass resting in the sand">
        <defs>
          <radialGradient id="objectTone" cx="50%" cy="45%" r="55%">
            <stop offset="0%" stop-color="var(--object-mid)"/>
            <stop offset="100%" stop-color="var(--object-dark)"/>
          </radialGradient>
        </defs>
        <ellipse cx="111" cy="122" rx="100" ry="84" fill="url(#objectTone)"/>
      </svg>
      <div class="author-name">DR. GAVIN TERLECKI</div>
    </section>
  </div>
</div>
</body>
</html>
```